Selvin: A Friday night in the Prophetic Flyer

We are holding 2 Friday night events, one on 10/25/19 and the other on 11/29/19.
The time frame is 6:30pm-9:00pm. These services will be a time of prayer/healing for the sick and will be prophetic as well. (There will be prophets prophesying over people)

The event is called: Selvin: A Friday night in the Prophetic
The flyer should also include the phrase/excerpt: "And they prophesied also".

Keywords/Phrases: Prophetic, Healing, Climbing in the Spirit, Higher level of Anointing...

Target Market(s)

those looking for healing, seeking a word from God

Colors

Designer to choose colors to be used in the design.

Requirements
Must have
• The event is called: Selvin: A Friday night in the Prophetic
• The flyer should also include the phrase/excerpt: "And they prophesied also".
• It must include the Tovik logo attached, either is fine, we have attached two different versions.
• It must have the dates, location, time
• Dates: October 25, 2019 and November 29, 2019
• Location: Hollard Community Center
• (Downtown Portland) 482 Wendle Street
• Portland, ME 04102
• Time: 6:30pm-9:00pm
• Contact Info: Tel. 207-555-3841
• email: contact@brimfield-hall.org
• web: www.tovik.org
Nice to have
• creativity in color scheme, the meaning of the word Selvin conveyed in a classy artistic way/design.
Should not have
• Crosses, pictures of churches

```html
<!DOCTYPE html>
<html lang="en">
<head>
<meta charset="utf-8">
<title>Selvin: A Friday Night in the Prophetic — Flyer</title>
<link rel="stylesheet" href="https://fonts.googleapis.com/css2?family=Cinzel:wght@400;600;700&family=Montserrat:ital,wght@0,600;0,700;1,800&family=Oswald:wght@500;600&family=Great+Vibes&display=swap">
<style>
  :root {
    --navy: #033a63;
    --navy-deep: #022c4d;
    --orange: #f7941d;
    --orange-deep: #e8820f;
    --sky: #8fd3e6;
    --royal: #0a6fc2;
    --page: #e9eef1;
    --white: #ffffff;
  }
  html, body {
    margin: 0;
    width: 1015px;
    height: 1200px;
    overflow: hidden;
    background: var(--page);
  }
  .flyer {
    position: absolute;
    left: 87px;
    top: 5px;
    width: 840px;
    height: 1190px;
    box-shadow: 0 4px 18px rgba(0, 0, 0, 0.18);
  }
  .flyer svg { display: block; width: 100%; height: 100%; }
  .brand-name { font-family: "Montserrat", sans-serif; font-weight: 700; fill: var(--white); }
  .theme-label { font-family: "Montserrat", sans-serif; font-weight: 700; fill: var(--navy); }
  .title { font-family: "Cinzel", serif; font-weight: 600; fill: var(--navy); }
  .title--accent { fill: var(--orange); }
  .banner-text { font-family: "Oswald", sans-serif; font-weight: 500; fill: var(--white); letter-spacing: 3px; }
  .date-month { font-family: "Oswald", sans-serif; font-weight: 600; fill: var(--navy); }
  .date-day { fill: var(--orange); }
  .ampersand { font-family: "Oswald", sans-serif; font-weight: 600; fill: var(--navy); }
  .time-label { font-family: "Cinzel", serif; font-weight: 600; fill: var(--navy); }
  .time-value { font-family: "Cinzel", serif; font-weight: 600; fill: var(--orange); }
  .contact-script { font-family: "Great Vibes", cursive; fill: var(--navy); }
  .contact-phone { font-family: "Montserrat", sans-serif; font-weight: 800; font-style: italic; fill: var(--navy); }
  .venue-text { font-family: "Montserrat", sans-serif; font-weight: 600; fill: var(--white); }
  .web-text { font-family: "Montserrat", sans-serif; font-weight: 600; fill: var(--white); }
</style>
</head>
<body>
<div class="flyer">
<svg viewBox="0 0 1200 1700" xmlns="http://www.w3.org/2000/svg">
  <defs>
    <linearGradient id="photoTone" x1="0" y1="0" x2="1" y2="0.4">
      <stop offset="0" stop-color="#120c0d"/>
      <stop offset="0.55" stop-color="#4a3033"/>
      <stop offset="0.8" stop-color="#c9b8bb"/>
      <stop offset="1" stop-color="#f4eef0"/>
    </linearGradient>
    <radialGradient id="medallion" cx="0.5" cy="0.4" r="0.6">
      <stop offset="0" stop-color="#1a8be0"/>
      <stop offset="1" stop-color="#0556a3"/>
    </radialGradient>
    <linearGradient id="themeBar" x1="0" y1="0" x2="1" y2="0">
      <stop offset="0" stop-color="#a9bcc8"/>
      <stop offset="1" stop-color="#e8f0f4"/>
    </linearGradient>
    <linearGradient id="bannerFade" x1="0" y1="0" x2="1" y2="0">
      <stop offset="0" stop-color="#033a63" stop-opacity="0"/>
      <stop offset="0.15" stop-color="#033a63"/>
      <stop offset="1" stop-color="#033a63"/>
    </linearGradient>
    <linearGradient id="timePill" x1="0" y1="0" x2="1" y2="0">
      <stop offset="0" stop-color="#ffffff"/>
      <stop offset="0.5" stop-color="#e4e6e8"/>
      <stop offset="1" stop-color="#ffffff"/>
    </linearGradient>
    <linearGradient id="footerOrange" x1="0" y1="0" x2="0" y2="1">
      <stop offset="0" stop-color="#f7941d"/>
      <stop offset="1" stop-color="#e8820f"/>
    </linearGradient>
  </defs>

  <!-- page base -->
  <rect class="page-base" width="1200" height="1700" fill="#ffffff"/>

  <!-- header -->
  <path class="header-navy" d="M0,0 H1200 V520 C950,560 700,560 450,520 C300,460 120,440 0,470 Z" fill="var(--navy)"/>
  <path class="header-sky" d="M450,540 C700,600 950,590 1200,520 V545 C950,610 700,620 450,560 Z" fill="var(--sky)"/>
  <path class="header-navy-band" d="M450,510 C700,560 950,540 1200,470 V520 C950,590 700,590 450,545 Z" fill="var(--navy)"/>
  <path class="header-orange-band" d="M740,0 H830 C700,180 560,300 420,360 L450,510 C700,545 950,520 1200,410 V470 C950,540 700,560 450,530 L380,360 C520,300 640,170 740,0 Z" fill="var(--orange)"/>
  <path class="header-photo" role="img" aria-label="Photograph: hands clasped in prayer holding prayer beads, lit from above"
        d="M830,0 H1200 V410 C950,520 700,545 450,510 L420,360 C560,300 700,180 830,0 Z" fill="url(#photoTone)"/>

  <!-- organiser name -->
  <text class="brand-name" x="100" y="200" font-size="80">Tovik</text>

  <!-- medallion -->
  <circle class="medallion-ring" cx="263" cy="484" r="198" fill="var(--orange)"/>
  <circle class="medallion-art" role="img" aria-label="Illustration: praying hands with prayer beads" cx="263" cy="484" r="175" fill="url(#medallion)"/>

  <!-- themes -->
  <g class="theme">
    <rect x="0" y="725" width="340" height="115" fill="url(#themeBar)"/>
    <text class="theme-label" x="35" y="797" font-size="42">Prophetic</text>
    <circle cx="348" cy="784" r="68" fill="var(--navy)"/>
    <circle role="img" aria-label="Icon: praying hands" cx="348" cy="784" r="55" fill="var(--orange)"/>
  </g>
  <g class="theme">
    <rect x="0" y="899" width="330" height="135" fill="url(#themeBar)"/>
    <text class="theme-label" x="42" y="980" font-size="42">Healing</text>
    <circle cx="342" cy="967" r="82" fill="var(--navy)"/>
    <circle role="img" aria-label="Icon: open hand" cx="342" cy="967" r="67" fill="var(--orange)"/>
  </g>
  <g class="theme">
    <rect x="0" y="1104" width="360" height="153" fill="url(#themeBar)"/>
    <text class="theme-label" x="145" y="1166" font-size="42" text-anchor="middle">Climbing</text>
    <text class="theme-label" x="145" y="1222" font-size="42" text-anchor="middle">in the Spirit</text>
    <circle cx="376" cy="1177" r="98" fill="var(--navy)"/>
    <circle role="img" aria-label="Icon: dove above an open book" cx="376" cy="1177" r="82" fill="var(--orange)"/>
  </g>
  <g class="theme">
    <rect x="0" y="1320" width="470" height="167" fill="url(#themeBar)"/>
    <text class="theme-label" x="190" y="1390" font-size="42" text-anchor="middle">Higher level</text>
    <text class="theme-label" x="180" y="1446" font-size="42" text-anchor="middle">of Anointing...</text>
    <circle cx="494" cy="1392" r="115" fill="var(--navy)"/>
    <circle role="img" aria-label="Icon: speaker at a lectern" cx="494" cy="1392" r="98" fill="var(--orange)"/>
  </g>

  <!-- title -->
  <text class="title" x="485" y="762" font-size="128" textLength="655" lengthAdjust="spacingAndGlyphs">A FRIDAY</text>
  <text class="title" x="490" y="860" font-size="90" textLength="645" lengthAdjust="spacingAndGlyphs">NIGHT IN THE</text>
  <text class="title title--accent" x="488" y="972" font-size="110" textLength="648" lengthAdjust="spacingAndGlyphs">PROPHETIC</text>

  <!-- scripture banner -->
  <rect class="banner" x="400" y="1012" width="800" height="75" fill="url(#bannerFade)"/>
  <text class="banner-text" x="1135" y="1067" font-size="40" text-anchor="end">AND THEY PROPHESIED ALSO</text>

  <!-- dates -->
  <text class="date-month" x="645" y="1165" font-size="72" textLength="407" lengthAdjust="spacingAndGlyphs">OCTOBER <tspan class="date-day">25, 2019</tspan></text>
  <text class="date-month" x="645" y="1245" font-size="72" textLength="407" lengthAdjust="spacingAndGlyphs">NOVEMBER <tspan class="date-day">29, 2019</tspan></text>
  <text class="ampersand" x="1066" y="1245" font-size="160" textLength="68" lengthAdjust="spacingAndGlyphs">&amp;</text>

  <!-- time -->
  <rect class="time-pill" x="680" y="1282" width="390" height="65" fill="url(#timePill)"/>
  <text class="time-label" x="870" y="1331" font-size="44" text-anchor="middle">- TIME -</text>
  <text class="time-value" x="885" y="1412" font-size="52" text-anchor="middle">6:30PM-9:00PM</text>

  <!-- contact -->
  <text x="612" y="1490"><tspan class="contact-script" font-size="56">Contact us </tspan><tspan class="contact-phone" font-size="40">207-555-3841</tspan></text>

  <!-- footer -->
  <path class="footer-sky" d="M700,1620 C900,1535 1050,1505 1200,1500 V1535 C1000,1540 850,1580 720,1640 Z" fill="var(--sky)"/>
  <path class="footer-navy" d="M560,1700 C700,1620 950,1540 1200,1530 V1700 Z" fill="var(--navy)"/>
  <path class="footer-orange" d="M0,1500 C300,1480 600,1530 820,1610 C600,1680 300,1700 0,1692 Z" fill="url(#footerOrange)"/>
  <path class="footer-shore" d="M0,1692 C300,1700 600,1680 820,1610 C620,1700 400,1700 0,1700 Z" fill="var(--navy)"/>

  <!-- venue -->
  <g class="pin-icon" fill="var(--navy)">
    <path d="M80,1555 a30,30 0 0 1 30,30 c0,22 -22,42 -30,70 c-8,-28 -30,-48 -30,-70 a30,30 0 0 1 30,-30 Z"/>
    <circle cx="80" cy="1585" r="13" fill="var(--orange)"/>
  </g>
  <text class="venue-text" x="128" y="1578" font-size="26">Hollard Community Center</text>
  <text class="venue-text" x="128" y="1613" font-size="26">(Downtown Portland) 482 Wendle Street</text>
  <text class="venue-text" x="128" y="1648" font-size="26">Portland, ME 04102</text>

  <!-- web + email -->
  <g class="globe-icon" fill="none" stroke="#ffffff" stroke-width="2">
    <circle cx="845" cy="1631" r="8"/>
    <ellipse cx="845" cy="1631" rx="3.5" ry="8"/>
    <line x1="837" y1="1631" x2="853" y2="1631"/>
  </g>
  <text class="web-text" x="865" y="1639" font-size="23">www.tovik.org</text>
  <g class="mail-icon" fill="none" stroke="#ffffff" stroke-width="2">
    <rect x="836" y="1657" width="18" height="13"/>
    <polyline points="836,1657 845,1665 854,1657"/>
  </g>
  <text class="web-text" x="865" y="1671" font-size="23">contact@brimfield-hall.org</text>
</svg>
</div>
</body>
</html>
```